Plomberie TRD est une nouvelle entreprise de plomberie

Jaimerais maintenant des carte daffaire

Tendance
Avec un petit Puntch

Jaimerais quelque chose dans ce style avec le logo foncé plomberie trd en facade
Jaimerais une photo en backgroung de fitting de plomberie comme je vous ai envoyer

Si vous voulez chercher une photo marquer sur google ( fitting kopran) pour vous donner des idee
Je veux que les fitting soit dune couleur pale en back ground pour faire ressortir mon logo

Toujours en facade de la carte je veux quil y ai mes services d'inscrit

Construction neuve
Reparation
Renovation
Urgence

438-261-5907
Bastien corriveau

A larriere de la carte jaimerais le logo pâle plomberie TRD
Avec mes info
Email: info.trdbatiment@exemplemail.com
Bastien corriveau
Cell: 438-261-5907
Plomberietrd.example

Voici des design que jai bien aimer libre a vous de vous laisser aller plus loin

Merci au plaisir de travailler avec vous

Target Market(s)

30 a 60 ans contracteur general

Industry/Entity Type

Construction plomberie

Contact Information for Business Card

Plomberie TRD inc. 438-261-5907 Bastien corriveau. Plombier. info.trdbatiment@exemplemail.com

Font styles to use
Sans Serif

Colors
0054AA
0677BA
7BADD7
CADEEF
E8F1F8
F0912C
F2A743
F7CA91
FBE8D2
FDF5EE
EE7325
F08F49
F5BC92
FAE3D3
FDF4ED

Requirements
Must have
• Plombier serieux et virile jaime la couleur cuivre comme les fitting
Nice to have
• Carte transparente

```html
<!DOCTYPE html>
<html lang="fr">
<head>
<meta charset="utf-8">
<title>Plomberie TRD – cartes d'affaires</title>
<link href="https://fonts.googleapis.com/css2?family=Open+Sans:wght@400;600;700&display=swap" rel="stylesheet">
<style>
  :root {
    --stage: #232323;
    --card-dark: #1e1e21;
    --card-white: #ffffff;
    --blue: #0677ba;
    --blue-deep: #0054aa;
    --copper: #ee7325;
    --copper-dark: #9c4a16;
    --copper-light: #f08f49;
    --text-light: #f4f4f4;
  }
  * { margin: 0; padding: 0; box-sizing: border-box; }
  html, body { width: 1200px; height: 780px; overflow: hidden; }
  body {
    background: var(--stage);
    font-family: "Open Sans", Arial, sans-serif;
    position: relative;
  }
  .card {
    position: absolute;
    top: 233px;
    width: 550px;
    height: 314px;
    overflow: hidden;
    box-shadow: 0 12px 30px rgba(0,0,0,.55);
  }
  .card--back { left: 30px; background: var(--card-dark); }
  .card--front { left: 620px; background: var(--card-dark); }

  /* back */
  .back-pattern {
    position: absolute; inset: 0;
    background:
      radial-gradient(ellipse 70% 60% at 75% 10%, rgba(200,200,200,.28), transparent 70%),
      linear-gradient(160deg, #2a2a2d 0%, #18181a 100%);
  }
  .back-brand {
    position: absolute;
    left: 392px; top: 168px;
    display: flex; align-items: center; gap: 6px;
    font-size: 12px; font-weight: 700;
    color: var(--blue);
  }
  .back-brand .mark { width: 8px; height: 8px; background: var(--copper); }

  /* front */
  .front-shape { position: absolute; inset: 0; }
  .front-brand {
    position: absolute;
    left: 352px; top: 138px;
    display: flex; align-items: center; gap: 8px;
    font-size: 22px; font-weight: 700;
    color: var(--copper);
    white-space: nowrap;
  }
  .front-brand .mark { width: 12px; height: 12px; background: var(--blue); }

  .identity {
    position: absolute; left: 26px; top: 50px;
    padding-left: 16px;
  }
  .identity::before {
    content: ""; position: absolute; left: 0; top: 4px;
    width: 8px; height: 52px;
    background: linear-gradient(90deg, var(--copper-dark), var(--copper-light), var(--copper-dark));
  }
  .name { font-size: 27px; font-weight: 700; line-height: 1.1; }
  .name .first { color: var(--blue); }
  .name .last { color: var(--copper); }
  .role { font-size: 13px; color: var(--text-light); margin-top: 2px; }

  .services { position: absolute; left: 58px; top: 128px; }
  .services h2 { font-size: 15px; font-weight: 700; color: var(--blue); letter-spacing: .3px; }
  .services ul { list-style: none; margin-top: 2px; }
  .services li {
    font-size: 13px; color: var(--text-light); line-height: 1.35;
    display: flex; align-items: center; gap: 7px;
  }
  .services li::before {
    content: ""; width: 7px; height: 7px; border-radius: 50%;
    background: var(--copper);
  }

  .contact { position: absolute; left: 58px; top: 226px; list-style: none; }
  .contact li {
    font-size: 12.5px; color: var(--text-light); line-height: 1.5;
    display: flex; align-items: center; gap: 8px;
  }
  .contact svg { width: 13px; height: 13px; flex: none; }
</style>
</head>
<body>

<section class="card card--back" aria-label="Verso de la carte">
  <div class="back-pattern" role="img" aria-label="Motif répété du logo Plomberie TRD en noir brillant"></div>
  <div class="back-brand"><span class="mark"></span>Plomberie TRD</div>
</section>

<section class="card card--front" aria-label="Recto de la carte">
  <svg class="front-shape" viewBox="0 0 550 314" preserveAspectRatio="none" aria-hidden="true">
    <defs>
      <linearGradient id="copperEdge" x1="0" y1="0" x2="1" y2="1">
        <stop offset="0" stop-color="#9c4a16"/>
        <stop offset=".4" stop-color="#f08f49"/>
        <stop offset=".7" stop-color="#b8561c"/>
        <stop offset="1" stop-color="#ee7325"/>
      </linearGradient>
    </defs>
    <path d="M318 0 C 270 90, 330 250, 470 314 L550 314 L550 0 Z" fill="url(#copperEdge)"/>
    <path d="M334 0 C 290 90, 345 245, 482 314 L550 314 L550 0 Z" fill="#ffffff"/>
  </svg>

  <div class="front-brand"><span class="mark"></span>Plomberie TRD</div>

  <div class="identity">
    <p class="name"><span class="first">Bastien</span> <span class="last">Corriveau</span></p>
    <p class="role">CEO/Director</p>
  </div>

  <div class="services">
    <h2>SERVICES</h2>
    <ul>
      <li>Repair</li>
      <li>Renovation</li>
      <li>Emergency</li>
      <li>New construction</li>
    </ul>
  </div>

  <ul class="contact">
    <li>
      <svg viewBox="0 0 24 24"><path fill="#0677ba" d="M6.6 10.8a15 15 0 0 0 6.6 6.6l2.2-2.2a1 1 0 0 1 1-.25 11.4 11.4 0 0 0 3.6.57 1 1 0 0 1 1 1V20a1 1 0 0 1-1 1A17 17 0 0 1 3 4a1 1 0 0 1 1-1h3.5a1 1 0 0 1 1 1c0 1.25.2 2.45.57 3.57a1 1 0 0 1-.25 1z"/></svg>
      438-261-5907
    </li>
    <li>
      <svg viewBox="0 0 24 24"><circle cx="12" cy="12" r="10" fill="none" stroke="#0677ba" stroke-width="2"/><path d="M2 12h20M12 2c3 3 3 17 0 20M12 2c-3 3-3 17 0 20" fill="none" stroke="#0677ba" stroke-width="1.6"/></svg>
      www.plomberietrd.example
    </li>
    <li>
      <svg viewBox="0 0 24 24"><rect x="2" y="5" width="20" height="14" rx="1.5" fill="none" stroke="#0677ba" stroke-width="2"/><path d="M2.5 6l9.5 7 9.5-7" fill="none" stroke="#0677ba" stroke-width="2"/></svg>
      info.trdbatiment@exemplemail.com
    </li>
  </ul>
</section>

</body>
</html>
```